We need a design for a Tequila line that will be infused with cannabis oil.
The design should have at least the following items.

The name Lumaro Tequila
Marijuana leaf
200 ml fluid
500 mg THC

The lable to be printed will be clear "see through"
The liquid inside the clear bottle will be light gold in color.

Target Market(s)

Marijuana users

Requirements
Must have
• Marijuana leaf
• must say 200 ml
• must say 500 mg thc
Nice to have
• bottle lable will be clear on clear bottle.

```html
<!DOCTYPE html>
<html lang="en">
<head>
<meta charset="utf-8">
<title>Lumaro Tequila – Label</title>
<link href="https://fonts.googleapis.com/css2?family=Bebas+Neue&family=Oswald:wght@500&display=swap" rel="stylesheet">
<style>
  :root{
    --page:#f8f8f9;
    --label-gold:#f5e07a;
    --label-edge:#fbf2c4;
    --ink:#0d0d0b;
    --leaf-green:#5f8a2a;
    --mandala-line:#fffbe6;
  }
  html,body{margin:0;padding:0;overflow:hidden;}
  body{width:1200px;height:1200px;background:var(--page);position:relative;}
  .label{
    position:absolute;left:174px;top:160px;width:852px;height:880px;
    background:radial-gradient(ellipse at 50% 50%, var(--label-gold) 45%, var(--label-edge) 100%);
    overflow:hidden;
  }
  .label__mandala{position:absolute;left:66px;top:60px;width:720px;height:720px;}
  .label__leaf{position:absolute;left:306px;top:250px;width:240px;height:240px;}
  .label__title{
    position:absolute;left:0;right:0;margin:0;text-align:center;
    font-family:"Bebas Neue",sans-serif;font-weight:400;color:var(--ink);line-height:1;
  }
  .label__title--top{top:196px;font-size:152px;transform:scaleY(1.19);transform-origin:top center;}
  .label__title--bottom{top:352px;font-size:137px;letter-spacing:-2px;transform:scaleY(2.1);transform-origin:top center;}
  .label__facts{
    position:absolute;left:0;right:0;top:680px;text-align:center;
    font-family:"Oswald",sans-serif;font-weight:500;color:var(--ink);font-size:27px;line-height:1;
  }
  .label__dose{display:block;}
  .label__rule{display:block;width:104px;height:3px;background:var(--ink);margin:12px auto 10px;}
  .label__volume{display:block;}
  .label__rule--end{margin:8px auto 0;}
</style>
</head>
<body>
  <section class="label" aria-label="Lumaro Tequila bottle label">
    <svg class="label__mandala" viewBox="0 0 720 720" role="img" aria-label="Decorative geometric mandala pattern">
      <defs>
        <radialGradient id="mandalaGlow" cx="50%" cy="50%" r="50%">
          <stop offset="0%" stop-color="#fff6c8" stop-opacity="0.55"/>
          <stop offset="100%" stop-color="#fff6c8" stop-opacity="0"/>
        </radialGradient>
      </defs>
      <circle cx="360" cy="360" r="360" fill="url(#mandalaGlow)"/>
    </svg>
    <svg class="label__leaf" viewBox="0 0 240 240" role="img" aria-label="Cannabis leaf illustration">
      <defs>
        <radialGradient id="leafTone" cx="50%" cy="55%" r="50%">
          <stop offset="0%" stop-color="#5f8a2a" stop-opacity="0.9"/>
          <stop offset="100%" stop-color="#5f8a2a" stop-opacity="0"/>
        </radialGradient>
      </defs>
      <circle cx="120" cy="120" r="120" fill="url(#leafTone)"/>
    </svg>
    <h1 class="label__title label__title--top">Lumaro</h1>
    <p class="label__title label__title--bottom">Tequila</p>
    <div class="label__facts">
      <span class="label__dose">500 MG THC</span>
      <span class="label__rule"></span>
      <span class="label__volume">200 ML</span>
      <span class="label__rule label__rule--end"></span>
    </div>
  </section>
</body>
</html>
```